Landingpage design for Movarabroker website

We need a design for a responsive 1 page landing page.
Good example: https://www.kelvaro.com/
On the homepage we will like to have a explanation video
attached you can find the logo's

About the website Movara.offers:
Movara.offers is a “Broker” we bring buyers and sellers together and facilitate transactions

Simple
quickly
Actuel
Compare (who is the best provider, at what price)
great offer
independent
1 invoice

Target Market(s)

BtoB

Number of Pages Required

1 page

Requirements
Must have
• On the homepage we will like to have a explanation video
Nice to have
• something between shipper and carrier and bring them togheter
• We will focus us first on fish transport... maybe you can add something
• Map from europe that shows our workarea

```html
<!DOCTYPE html>
<html lang="en">
<head>
<meta charset="utf-8">
<title>Movara.offers – Landing page</title>
<link href="https://fonts.googleapis.com/css2?family=Open+Sans:wght@400;600;700&display=swap" rel="stylesheet">
<style>
  :root{
    --brand:#2fa9d6;
    --brand-dark:#1e8fbf;
    --ink:#1d1d1d;
    --text:#7a7a7a;
    --muted:#9a9a9a;
    --gray:#f4f4f4;
    --line:#e4e4e4;
    --dark:#2e2e2e;
    --white:#ffffff;
  }
  *{box-sizing:border-box;margin:0;padding:0}
  html,body{width:1200px;height:3279px;overflow:hidden}
  body{font-family:"Open Sans",Arial,sans-serif;color:var(--text);background:var(--white)}
  .container{width:936px;margin:0 auto;position:relative}

  /* Header */
  .site-header{height:79px;background:var(--brand);color:var(--white)}
  .site-header .container{height:79px;display:flex;align-items:center}
  .brand{display:flex;align-items:center;gap:12px;font-size:19px;font-weight:600;color:var(--white);width:361px}
  .brand-dot{width:34px;height:34px;border-radius:50%;border:3px solid var(--white)}
  .main-nav{display:flex;gap:34px;font-size:12px;font-weight:600;width:397px}
  .account-nav{display:flex;gap:26px;font-size:12px;font-weight:600;margin-right:26px}
  .header-icons{display:flex;gap:20px;align-items:center}

  /* Hero */
  .hero{height:537px;background:var(--gray);padding-top:140px}
  .hero .container{display:flex;justify-content:space-between}
  .hero-copy{width:440px;padding-top:18px}
  .hero-title{font-size:27px;line-height:34px;font-weight:700;color:var(--ink)}
  .hero-lead{font-size:15px;line-height:22px;color:#444;margin-top:10px;width:400px}
  .hero .btn{margin-top:28px}
  .video{width:440px;height:255px;position:relative;
    background:linear-gradient(135deg,#7d6a52 0%,#b9bec4 35%,#d6dadf 55%,#8f9aa3 75%,#6a5843 100%)}
  .play{position:absolute;left:50%;top:50%;transform:translate(-50%,-50%)}

  /* Button */
  .btn{display:flex;align-items:center;width:405px;height:83px;padding:0 26px;background:var(--brand);
    color:var(--white);font-size:15.5px;line-height:22px}
  .btn svg{display:inline-block;vertical-align:middle;margin-left:6px}

  /* Feature sections */
  .feature{height:440px;padding-top:89px}
  .feature.alt{background:var(--gray);height:441px}
  .feature .container{display:flex;justify-content:space-between;height:256px}
  .feature-copy{width:444px;height:256px;display:flex;flex-direction:column}
  .feature-title{font-size:24px;font-weight:600;color:var(--brand);line-height:30px;margin-top:6px}
  .feature-text{font-size:12.4px;line-height:19.6px;margin-top:10px;color:var(--text)}
  .feature-copy .btn{margin-top:auto}
  .media{position:relative;width:456px;height:256px}
  .media .shot{position:absolute;inset:0}
  .media .stripe{position:absolute;inset:0}
  .media-left .shot{clip-path:polygon(0 0,443px 0,363px 100%,0 100%)}
  .media-right .shot{clip-path:polygon(13px 0,100% 0,100% 100%,37px 100%)}

  .shot-transport{background:linear-gradient(160deg,#f6c06a 0%,#e77f2c 35%,#7a3a22 70%,#2e2220 100%)}
  .shot-trucks{background:linear-gradient(180deg,#6f8fb5 0%,#d8b487 45%,#9a9ea6 70%,#6b6f75 100%)}
  .shot-europe{background:linear-gradient(135deg,#ececec 0%,#4a4a4a 40%,#2f2f2f 70%,#e6e6e6 100%)}
  .shot-fish{background:linear-gradient(135deg,#3c4f79 0%,#e3e6ea 40%,#9aa6b4 65%,#f1f1f1 100%)}
  .shot-map{background:linear-gradient(135deg,#a6c9e8 0%,#dfe5d6 45%,#e8e0c8 70%,#b7d3ea 100%)}

  /* Footer */
  .footer-top{height:223px;background:var(--gray);border-bottom:1px solid var(--line)}
  .footer-top .container{display:flex;padding-top:68px}
  .footer-about{width:398px}
  .footer-about h3{font-size:19px;font-weight:600;color:var(--ink)}
  .footer-about p{font-size:10.5px;line-height:17px;margin-top:12px;width:330px}
  .footer-col{width:176px}
  .footer-col:last-child{width:auto;margin-left:58px}
  .icon-badge{width:40px;height:40px;border-radius:50%;background:var(--brand);display:flex;align-items:center;justify-content:center}
  .footer-col h4{font-size:13px;font-weight:600;color:var(--ink);margin-top:10px}
  .footer-col ul{list-style:none;font-size:10.5px;line-height:17px;margin-top:6px}
  .social{display:flex;gap:7px;margin-top:8px}
  .social span{width:22px;height:22px;border-radius:50%;background:var(--brand-dark)}

  .footer-links{height:159px;background:var(--white)}
  .footer-links .container{display:flex;padding-top:62px}
  .info-col{width:243px}
  .info-col h5{font-size:13px;font-weight:600;color:var(--ink);display:flex;align-items:center;gap:8px}
  .info-col p{font-size:10px;line-height:14px;margin-top:4px;width:190px}

  .footer-bottom{height:81px;background:var(--dark);color:#bdbdbd;text-align:center;padding-top:19px}
  .bottom-nav{font-size:10.5px}
  .bottom-nav span{margin:0 7px}
  .copyright{font-size:10.5px;margin-top:9px}
</style>
</head>
<body>

<header class="site-header">
  <div class="container">
    <div class="brand"><span class="brand-dot"></span>Movara.offers</div>
    <nav class="main-nav"><span>About Us</span><span>Pricing</span><span>FAQ</span><span>Contact</span></nav>
    <nav class="account-nav"><span>Login</span><span>Register</span></nav>
    <div class="header-icons">
      <svg width="18" height="18" viewBox="0 0 18 18"><circle cx="7.5" cy="7.5" r="5.5" fill="none" stroke="#fff" stroke-width="2.5"/><line x1="11.5" y1="11.5" x2="16.5" y2="16.5" stroke="#fff" stroke-width="3" stroke-linecap="round"/></svg>
      <svg width="18" height="16" viewBox="0 0 18 16"><rect y="1" width="18" height="3" fill="#fff"/><rect y="7" width="18" height="3" fill="#fff"/><rect y="13" width="18" height="3" fill="#fff"/></svg>
    </div>
  </div>
</header>

<section class="hero">
  <div class="container">
    <div class="hero-copy">
      <h1 class="hero-title">Looking for a transport company?<br>Looking for a loading?</h1>
      <p class="hero-lead">We bring you together and find the best and most efficient way for you shipments</p>
      <a class="btn">You are a view steps away from the easiest way to organize your transports.
        <svg width="11" height="10" viewBox="0 0 11 10"><path d="M0 4h7V1l4 4-4 4V6H0z" fill="#fff"/></svg></a>
    </div>
    <div class="video" role="img" aria-label="Explanation video: crates of fresh fish on ice">
      <svg class="play" width="46" height="46" viewBox="0 0 46 46"><circle cx="23" cy="23" r="23" fill="#fff"/><path d="M18 13l14 10-14 10z" fill="#111"/></svg>
    </div>
  </div>
</section>

<section class="feature">
  <div class="container">
    <div class="media media-left">
      <div class="shot shot-transport" role="img" aria-label="Cargo plane over a freight train at sunset"></div>
      <svg class="stripe" width="456" height="256" viewBox="0 0 456 256"><polygon points="443,0 451,0 371,256 363,256" fill="var(--brand-dark)"/></svg>
    </div>
    <div class="feature-copy">
      <h2 class="feature-title">Why should i use Movara.offers?</h2>
      <p class="feature-text">Nam a lectus vitae erat ornare tempus. Cum sociis natoque penatibus et magnis dis parturient montes, nascetur ridiculus mus. Duis sed velit a lacus imperdiet aliquam vitae vehicula dolor. Cum sociis natoque penatibus et magnis dis parturient montes, nascetur ridiculus mus. Etiam vestibulum odio non laoreet semper. Cras rhoncus, odio eget finibus dictum, ligula sem tempus magna, in lacinia sapien tellus ac neque.</p>
      <a class="btn">You are a view steps away from the easiest way to organize your transports.
        <svg width="11" height="10" viewBox="0 0 11 10"><path d="M0 4h7V1l4 4-4 4V6H0z" fill="#fff"/></svg></a>
    </div>
  </div>
</section>

<section class="feature alt">
  <div class="container">
    <div class="feature-copy">
      <h2 class="feature-title">Transport Solutions</h2>
      <p class="feature-text">Nam a lectus vitae erat ornare tempus. Cum sociis natoque penatibus et magnis dis parturient montes, nascetur ridiculus mus. Duis sed velit a lacus imperdiet aliquam vitae vehicula dolor. Cum sociis natoque penatibus et magnis dis parturient montes, nascetur ridiculus mus. Etiam vestibulum odio non laoreet semper. Cras rhoncus, odio eget finibus dictum, ligula sem tempus magna, in lacinia sapien tellus ac neque.</p>
      <a class="btn">You are a view steps away from the easiest way to organize your transports.
        <svg width="11" height="10" viewBox="0 0 11 10"><path d="M0 4h7V1l4 4-4 4V6H0z" fill="#fff"/></svg></a>
    </div>
    <div class="media media-right">
      <div class="shot shot-trucks" role="img" aria-label="Row of trucks parked under an evening sky"></div>
      <svg class="stripe" width="456" height="256" viewBox="0 0 456 256"><polygon points="3,0 11,0 35,256 27,256" fill="var(--brand-dark)"/></svg>
    </div>
  </div>
</section>

<section class="feature">
  <div class="container">
    <div class="media media-left">
      <div class="shot shot-europe" role="img" aria-label="Map of Europe with location pins marking the work area"></div>
      <svg class="stripe" width="456" height="256" viewBox="0 0 456 256"><polygon points="443,0 451,0 371,256 363,256" fill="var(--brand-dark)"/></svg>
    </div>
    <div class="feature-copy">
      <h2 class="feature-title">Destination Europe</h2>
      <p class="feature-text">Nam a lectus vitae erat ornare tempus. Cum sociis natoque penatibus et magnis dis parturient montes, nascetur ridiculus mus. Duis sed velit a lacus imperdiet aliquam vitae vehicula dolor. Cum sociis natoque penatibus et magnis dis parturient montes, nascetur ridiculus mus. Etiam vestibulum odio non laoreet semper. Cras rhoncus, odio eget finibus dictum, ligula sem tempus magna, in lacinia sapien tellus ac neque.</p>
      <a class="btn">You are a view steps away from the easiest way to organize your transports.
        <svg width="11" height="10" viewBox="0 0 11 10"><path d="M0 4h7V1l4 4-4 4V6H0z" fill="#fff"/></svg></a>
    </div>
  </div>
</section>

<section class="feature alt">
  <div class="container">
    <div class="feature-copy">
      <h2 class="feature-title">Free?</h2>
      <p class="feature-text">Nam a lectus vitae erat ornare tempus. Cum sociis natoque penatibus et magnis dis parturient montes, nascetur ridiculus mus. Duis sed velit a lacus imperdiet aliquam vitae vehicula dolor. Cum sociis natoque penatibus et magnis dis parturient montes, nascetur ridiculus mus. Etiam vestibulum odio non laoreet semper. Cras rhoncus, odio eget finibus dictum, ligula sem tempus magna, in lacinia sapien tellus ac neque.</p>
      <a class="btn">You are a view steps away from the easiest way to organize your transports.
        <svg width="11" height="10" viewBox="0 0 11 10"><path d="M0 4h7V1l4 4-4 4V6H0z" fill="#fff"/></svg></a>
    </div>
    <div class="media media-right">
      <div class="shot shot-fish" role="img" aria-label="Fresh salmon in a white polystyrene transport box"></div>
      <svg class="stripe" width="456" height="256" viewBox="0 0 456 256"><polygon points="3,0 11,0 35,256 27,256" fill="var(--brand-dark)"/></svg>
    </div>
  </div>
</section>

<section class="feature">
  <div class="container">
    <div class="media media-left">
      <div class="shot shot-map" role="img" aria-label="Road map of Europe showing the office location"></div>
      <svg class="stripe" width="456" height="256" viewBox="0 0 456 256"><polygon points="443,0 451,0 371,256 363,256" fill="var(--brand-dark)"/></svg>
    </div>
    <div class="feature-copy">
      <h2 class="feature-title">Contact</h2>
      <p class="feature-text">Nam a lectus vitae erat ornare tempus. Cum sociis natoque penatibus et magnis dis parturient montes, nascetur ridiculus mus. Duis sed velit a lacus imperdiet aliquam vitae vehicula dolor. Cum sociis natoque penatibus et magnis dis parturient montes, nascetur ridiculus mus. Etiam vestibulum odio non laoreet semper. Cras rhoncus, odio eget finibus dictum, ligula sem tempus magna, in lacinia sapien tellus ac neque.</p>
      <a class="btn">You are a view steps away from the easiest way to organize your transports.
        <svg width="11" height="10" viewBox="0 0 11 10"><path d="M0 4h7V1l4 4-4 4V6H0z" fill="#fff"/></svg></a>
    </div>
  </div>
</section>

<footer>
  <div class="footer-top">
    <div class="container">
      <div class="footer-about">
        <h3>Movara.offers</h3>
        <p>Nam a lectus vitae erat ornare tempus. Cum sociis natoque penatibus et magnis dis parturient montes, nascetur ridiculus mus. Duis sed velit a lacus imperdiet aliquam vitae vehicula dolor. Cum sociis natoque penatibus et magnis dis parturient montes.</p>
      </div>
      <div class="footer-col">
        <div class="icon-badge"><svg width="16" height="16" viewBox="0 0 16 16"><rect x="1" y="6" width="9" height="5" rx="2.5" fill="none" stroke="#fff" stroke-width="1.8" transform="rotate(-45 5.5 8.5)"/><rect x="6" y="5" width="9" height="5" rx="2.5" fill="none" stroke="#fff" stroke-width="1.8" transform="rotate(-45 10.5 7.5)"/></svg></div>
        <h4>Want more?</h4>
        <ul><li>Services</li><li>Transports</li><li>News</li></ul>
      </div>
      <div class="footer-col">
        <div class="icon-badge"><svg width="12" height="18" viewBox="0 0 12 18"><rect x="1" y="1" width="10" height="16" rx="2" fill="none" stroke="#fff" stroke-width="1.8"/><circle cx="6" cy="14" r="1" fill="#fff"/></svg></div>
        <h4>Talk to us</h4>
        <ul><li>Call : 555 204 7391</li><li>Email : info@movaraoffers.com</li></ul>
      </div>
      <div class="footer-col">
        <div class="icon-badge"><svg width="16" height="16" viewBox="0 0 16 16"><circle cx="12" cy="3.5" r="2.3" fill="#fff"/><circle cx="4" cy="8" r="2.3" fill="#fff"/><circle cx="12" cy="12.5" r="2.3" fill="#fff"/><path d="M12 3.5L4 8l8 4.5" stroke="#fff" stroke-width="1.4" fill="none"/></svg></div>
        <h4>Stay in touch</h4>
        <div class="social"><span></span><span></span><span></span><span></span></div>
      </div>
    </div>
  </div>

  <div class="footer-links">
    <div class="container">
      <div class="info-col">
        <h5><svg width="12" height="12" viewBox="0 0 12 12"><path d="M6 0l6 3v6l-6 3-6-3V3z" fill="var(--ink)"/></svg>Services</h5>
        <p>Curabitur dictum vitae ipsum quis elementum. Sed vel suscipit nisl.</p>
      </div>
      <div class="info-col">
        <h5><svg width="12" height="12" viewBox="0 0 12 12"><rect x="0" y="3" width="12" height="9" rx="1" fill="var(--ink)"/><rect x="4" y="0.5" width="4" height="3" fill="none" stroke="var(--ink)" stroke-width="1.2"/></svg>Career</h5>
        <p>Curabitur dictum vitae ipsum quis elementum. Sed vel suscipit nisl.</p>
      </div>
      <div class="info-col">
        <h5><svg width="12" height="12" viewBox="0 0 12 12"><rect x="1" y="0.5" width="10" height="11" fill="none" stroke="var(--ink)" stroke-width="1.2"/><path d="M3 4h6M3 6h6M3 8h4" stroke="var(--ink)" stroke-width="1"/></svg>Terms and Conditions</h5>
        <p>Curabitur dictum vitae ipsum quis elementum. Sed vel suscipit nisl.</p>
      </div>
      <div class="info-col">
        <h5><svg width="12" height="12" viewBox="0 0 12 12"><path d="M2 0.5h5l3 3v8H2z" fill="none" stroke="var(--ink)" stroke-width="1.2"/><path d="M4 6h4M4 8h4" stroke="var(--ink)" stroke-width="1"/></svg>Privacy Policy</h5>
        <p>Curabitur dictum vitae ipsum quis elementum. Sed vel suscipit nisl.</p>
      </div>
    </div>
  </div>

  <div class="footer-bottom">
    <nav class="bottom-nav">Home<span>|</span>About Us<span>|</span>Pricing<span>|</span>FAQ<span>|</span>Contact<span>|</span>Login<span>|</span>Register</nav>
    <p class="copyright">Copyright © 2017 Company name. All rights reserved.</p>
  </div>
</footer>

</body>
</html>
```